Luxury Ayurvedic Hair Oil logo and package design

We need a logo and package design for our Ayurvedic and natural hair growth oil. Our company, Velmora, is the premier luxury Ayurvedic beauty brand, bringing ancient East-Indian natural and botanic health and beauty products to the US market. Our first major product - Velmora Hair Growth Oil - is a coconut oil based product that was developed by tribes in the Southern State of Kerala that includes ancient herbs like Gooseberry, Indigo, Indian Aloe, Balloon Vine and Brahmi.

The design should be catered to the high-end luxury market (minimal design, minimal text, fonts that invoke a sense of luxury). The primary colors should be deep blue for the packaging and gold for the characters (it's in the name - Velmora). We are looking to sell our products in Brenvale and Tolland Pryce and require packaging that is in line with products sold at these high-end retailers.

The final logo design and packaging should communicate luxury and the ancient wisdom of far-eastern traditions.

Target Market(s)

Velmora's main target is women who value fashionable/quality skincare, beauty, and fragrance products and are open to a medium to high price range. These women love uniqueness in brand and products that cannot be found elsewhere. They are looking for the next new "it" item that will take their haircare and beauty regiment to the next level.

Industry/Entity Type

Hair And Beauty

Font styles to use
Serif

Colors
2f73b3
ffc214

Requirements
Must have
• Must use deep blue (royal blue) background and gold text (to align with brand name). Must use luxurious fonts
Nice to have
• Flowers or other natural symbols, pictures that blend well with the product theme

```html
<!DOCTYPE html>
<html lang="en">
<head>
<meta charset="utf-8">
<title>Velmora Hair Growth Oil – Label</title>
<link rel="stylesheet" href="https://fonts.googleapis.com/css2?family=Bodoni+Moda:wght@500&family=Montserrat:wght@300&display=swap">
<style>
  :root {
    --page: #ffffff;
    --royal-blue: #323a8c;
    --botanical-blue: #2f73b3;
    --gold: #edbb30;
    --label-white: #ffffff;
  }
  * { margin: 0; padding: 0; box-sizing: border-box; }
  html, body {
    width: 807px;
    height: 1200px;
    overflow: hidden;
    background: var(--page);
  }
  .canvas {
    position: relative;
    width: 807px;
    height: 1200px;
  }
  .label {
    position: absolute;
    left: 179px;
    top: 166px;
    width: 449px;
    height: 868px;
    background: var(--royal-blue);
  }
  .botanical-wreath {
    position: absolute;
    left: 42px;
    top: 42px;
    width: 374px;
    height: 452px;
    border-radius: 46% 42% 40% 44%;
    background: radial-gradient(ellipse at center,
      rgba(47, 115, 179, 0.45) 0%,
      rgba(47, 115, 179, 0.28) 55%,
      rgba(47, 115, 179, 0) 80%);
  }
  .brand-frame {
    position: absolute;
    left: 98px;
    top: 102px;
    width: 254px;
    height: 321px;
    border: 2px solid var(--gold);
    background: var(--royal-blue);
  }
  .brand-dot {
    position: absolute;
    left: 50%;
    top: 44px;
    width: 96px;
    height: 96px;
    margin-left: -48px;
    border-radius: 50%;
    background: var(--gold);
  }
  .brand-name {
    position: absolute;
    left: 26px;
    right: 26px;
    top: 196px;
    display: flex;
    justify-content: space-between;
    font-family: "Bodoni Moda", "Didot", serif;
    font-weight: 500;
    color: var(--gold);
    font-size: 40px;
    line-height: 1;
    transform: scaleY(1.6);
    transform-origin: center top;
  }
  .product-name {
    position: absolute;
    left: 0;
    right: 0;
    top: 741px;
    text-align: center;
    font-family: "Montserrat", "Helvetica Neue", sans-serif;
    font-weight: 300;
    font-size: 20px;
    letter-spacing: 0.42em;
    padding-left: 0.42em;
    color: var(--label-white);
  }
</style>
</head>
<body>
  <main class="canvas">
    <section class="label">
      <div class="botanical-wreath" role="img" aria-label="Line-drawn wreath of palm fronds, coconuts, hibiscus flowers and gooseberries"></div>
      <div class="brand-frame">
        <span class="brand-dot" aria-hidden="true"></span>
        <h1 class="brand-name" aria-label="Velmora">
          <span aria-hidden="true">V</span><span aria-hidden="true">E</span><span aria-hidden="true">L</span><span aria-hidden="true">M</span><span aria-hidden="true">O</span><span aria-hidden="true">R</span><span aria-hidden="true">A</span>
        </h1>
      </div>
      <p class="product-name">HAIR GROWTH OIL</p>
    </section>
  </main>
</body>
</html>
```